Essential Capacities Mouse Mat

Seeking to design a mouse mat for distribution to employees that captures the Essential Capacities (see attached file).
The design should embody the 7 categories, be visual, ideally be icon based.

Mouse mat size:
9.25" x 7.68"
235 x 195 mm
2776 x 2303 pixels

Fonts:
Linden Harbor Academy (Arial)
LINDEN HARBOR ACADEMY (Agency FB, bold/all capitals)

Font styles to use
Sans Serif

Colors
0455a3
ffc214
6b449b
ec1f27
f37122
9bcb3b

Requirements
Must have
• The 7 Essential Capacities Headings must be incorporated in the design.

```html
<!DOCTYPE html>
<html lang="en">
<head>
<meta charset="utf-8">
<title>Essential Capacities Mouse Mat</title>
<link rel="stylesheet" href="https://fonts.googleapis.com/css2?family=Jost:wght@600;700&family=Arimo:wght@400&display=swap">
<style>
  :root{
    --page:#ffffff;
    --blue:#0455a3; --blue-light:#6ab4f5;
    --green:#9bcb3b; --green-dark:#5b8414;
    --yellow:#ffc214; --yellow-dark:#7d5a0c;
    --mint:#33e08a; --mint-dark:#075a2e;
    --orange:#f37122; --orange-dark:#b04e14;
    --purple:#6b449b; --purple-light:#d4aef5;
    --red:#ec1f27; --red-dark:#9b1017;
  }
  html,body{margin:0;padding:0;overflow:hidden;background:var(--page);}
  .mat{position:relative;width:1200px;height:1000px;overflow:hidden;background:var(--page);}
  .card{position:absolute;width:324px;height:268px;display:block;}
  .card .bg{fill:var(--bg);}
  .card .band{fill:var(--band);}
  .card .headline{fill:var(--ink);font:700 36px "Jost",sans-serif;}
  .card .band-line{fill:var(--band-ink);font:700 24px "Jost",sans-serif;}
  .card .sub-line{fill:var(--ink);font:700 18px "Jost",sans-serif;}
  .card .school-name{fill:var(--ink);font:700 9px "Jost",sans-serif;letter-spacing:0.4px;}
  .card .footer-name{fill:var(--ink);font:400 6px "Arimo",sans-serif;opacity:.8;}
  .card .icon{fill:var(--ink);stroke:none;}
  .card .icon-line{fill:none;stroke:var(--ink);}
  .card .icon-cut{fill:var(--bg);}

  .card--analytical{left:72px;top:45px;--bg:var(--blue);--band:var(--blue-light);--ink:var(--blue-light);--band-ink:var(--blue);}
  .card--adaptability{left:455px;top:45px;--bg:var(--green);--band:var(--green-dark);--ink:var(--green-dark);--band-ink:var(--green);}
  .card--communication{left:818px;top:45px;--bg:var(--yellow);--band:var(--yellow-dark);--ink:var(--yellow-dark);--band-ink:var(--yellow);}
  .card--integrity{left:72px;top:374px;--bg:var(--mint);--band:var(--mint-dark);--ink:var(--mint-dark);--band-ink:var(--mint);}
  .card--global{left:455px;top:374px;--bg:var(--orange);--band:var(--orange-dark);--ink:var(--orange-dark);--band-ink:var(--orange);}
  .card--leadership{left:818px;top:374px;--bg:var(--purple);--band:var(--purple-light);--ink:var(--purple-light);--band-ink:var(--purple);}
  .card--digital{left:455px;top:684px;--bg:var(--red);--band:var(--red-dark);--ink:var(--red-dark);--band-ink:var(--red);}
</style>
</head>
<body>
<main class="mat">

  <!-- Analytical -->
  <svg class="card card--analytical" viewBox="0 0 324 268" aria-labelledby="t1">
    <title id="t1">Analytical, creative thinking, problem-solving</title>
    <rect class="bg" width="324" height="268"/>
    <g class="icon-set">
      <g class="icon-line" stroke-width="3" stroke-linecap="round">
        <line x1="262" y1="12" x2="262" y2="20"/><line x1="236" y1="22" x2="241" y2="28"/><line x1="288" y1="22" x2="283" y2="28"/>
        <line x1="222" y1="48" x2="230" y2="48"/><line x1="294" y1="48" x2="302" y2="48"/>
        <line x1="228" y1="70" x2="234" y2="66"/><line x1="296" y1="70" x2="290" y2="66"/>
      </g>
      <path class="icon" d="M262 28a23 23 0 0 0-13 42v8h26v-8a23 23 0 0 0-13-42z"/>
      <rect class="icon" x="250" y="81" width="24" height="5" rx="2"/>
      <rect class="icon" x="253" y="89" width="18" height="5" rx="2"/>
      <rect class="icon-cut" x="259" y="37" width="6" height="20" rx="2"/>
      <circle class="icon-cut" cx="262" cy="64" r="3.5"/>
    </g>
    <g transform="rotate(-16.3 310 135)">
      <rect class="band" x="-120" y="135" width="600" height="44"/>
      <text class="headline" x="320" y="129" text-anchor="end" textLength="236" lengthAdjust="spacingAndGlyphs">ANALYTICAL</text>
      <text class="band-line" x="304" y="166" text-anchor="end" textLength="245" lengthAdjust="spacingAndGlyphs">CREATIVE THINKING</text>
      <text class="sub-line" x="291" y="201" text-anchor="end" textLength="197" lengthAdjust="spacingAndGlyphs">PROBLEM-SOLVING</text>
    </g>
    <text class="school-name" x="14" y="174">LINDEN</text>
    <text class="school-name" x="14" y="185">HARBOR</text>
    <text class="school-name" x="14" y="196">ACADEMY</text>
    <text class="footer-name" x="312" y="262" text-anchor="end">Linden Harbor Academy</text>
  </svg>

  <!-- Adaptability -->
  <svg class="card card--adaptability" viewBox="0 0 324 268" aria-labelledby="t2">
    <title id="t2">Adaptability, initiative and risk-taking</title>
    <rect class="bg" width="324" height="268"/>
    <g class="icon-set">
      <rect class="icon" x="226" y="68" width="70" height="22" rx="9"/>
      <circle class="icon" cx="261" cy="46" r="22"/>
      <circle class="icon-cut" cx="261" cy="46" r="16"/>
      <circle class="icon" cx="261" cy="46" r="11"/>
      <circle class="icon-cut" cx="261" cy="46" r="6"/>
      <circle class="icon" cx="261" cy="46" r="3"/>
      <line class="icon-line" x1="261" y1="46" x2="284" y2="24" stroke-width="3"/>
      <path class="icon" d="M282 20l8-3-3 8-4 1z"/>
    </g>
    <g transform="rotate(-16.3 310 135)">
      <rect class="band" x="-120" y="135" width="600" height="44"/>
      <text class="headline" x="319" y="129" text-anchor="end" textLength="255" lengthAdjust="spacingAndGlyphs">ADAPTABILITY</text>
      <text class="band-line" x="277" y="166" text-anchor="end" textLength="191" lengthAdjust="spacingAndGlyphs">INITIATIVE AND</text>
      <text class="sub-line" x="260" y="201" text-anchor="end" textLength="130" lengthAdjust="spacingAndGlyphs">RISK-TAKING</text>
    </g>
    <text class="school-name" x="14" y="174">LINDEN</text>
    <text class="school-name" x="14" y="185">HARBOR</text>
    <text class="school-name" x="14" y="196">ACADEMY</text>
    <text class="footer-name" x="312" y="262" text-anchor="end">Linden Harbor Academy</text>
  </svg>

  <!-- Complex communication -->
  <svg class="card card--communication" viewBox="0 0 324 268" aria-labelledby="t3">
    <title id="t3">Complex communication, oral and written</title>
    <rect class="bg" width="324" height="268"/>
    <g class="icon-set">
      <circle class="icon" cx="234" cy="30" r="9"/>
      <path class="icon" d="M222 42h24v28h-4v32h-7v-26h-2v26h-7v-32h-4z"/>
      <circle class="icon" cx="288" cy="30" r="9"/>
      <path class="icon" d="M276 42h24v28h-4v32h-7v-26h-2v26h-7v-32h-4z"/>
      <circle class="icon" cx="263" cy="14" r="12"/>
      <path class="icon" d="M254 22l-6 10 12-6z"/>
      <rect class="icon-cut" x="256" y="9" width="14" height="2.5"/>
      <rect class="icon-cut" x="256" y="15" width="14" height="2.5"/>
    </g>
    <g transform="rotate(-16.3 310 135)">
      <rect class="band" x="-120" y="135" width="600" height="44"/>
      <text class="headline" x="295" y="129" text-anchor="end" textLength="189" lengthAdjust="spacingAndGlyphs">COMPLEX</text>
      <text class="band-line" x="299" y="166" text-anchor="end" textLength="237" lengthAdjust="spacingAndGlyphs">COMMUNICATION</text>
      <text class="sub-line" x="290" y="201" text-anchor="end" textLength="194" lengthAdjust="spacingAndGlyphs">ORAL AND WRITTEN</text>
    </g>
    <text class="school-name" x="14" y="174">LINDEN</text>
    <text class="school-name" x="14" y="185">HARBOR</text>
    <text class="school-name" x="14" y="196">ACADEMY</text>
    <text class="footer-name" x="312" y="262" text-anchor="end">Linden Harbor Academy</text>
  </svg>

  <!-- Integrity -->
  <svg class="card card--integrity" viewBox="0 0 324 268" aria-labelledby="t4">
    <title id="t4">Integrity and ethical decision-making</title>
    <rect class="bg" width="324" height="268"/>
    <g class="icon-set">
      <circle class="icon" cx="256" cy="22" r="5"/>
      <rect class="icon" x="253" y="24" width="6" height="62"/>
      <rect class="icon" x="222" y="27" width="68" height="5" rx="2"/>
      <rect class="icon" x="236" y="86" width="40" height="8" rx="2"/>
      <g class="icon-line" stroke-width="1.5">
        <line x1="226" y1="32" x2="215" y2="62"/><line x1="226" y1="32" x2="237" y2="62"/>
        <line x1="286" y1="32" x2="275" y2="62"/><line x1="286" y1="32" x2="297" y2="62"/>
      </g>
      <path class="icon" d="M211 62h30a15 12 0 0 1-30 0z"/>
      <path class="icon" d="M271 62h30a15 12 0 0 1-30 0z"/>
    </g>
    <g transform="rotate(-16.3 310 135)">
      <rect class="band" x="-120" y="135" width="600" height="44"/>
      <text class="headline" x="284" y="129" text-anchor="end" textLength="186" lengthAdjust="spacingAndGlyphs">INTEGRITY</text>
      <text class="band-line" x="268" y="166" text-anchor="end" textLength="167" lengthAdjust="spacingAndGlyphs">AND ETHICAL</text>
      <text class="sub-line" x="291" y="201" text-anchor="end" textLength="197" lengthAdjust="spacingAndGlyphs">DECISION-MAKING</text>
    </g>
    <text class="school-name" x="14" y="174">LINDEN</text>
    <text class="school-name" x="14" y="185">HARBOR</text>
    <text class="school-name" x="14" y="196">ACADEMY</text>
    <text class="footer-name" x="312" y="262" text-anchor="end">Linden Harbor Academy</text>
  </svg>

  <!-- Global perspective -->
  <svg class="card card--global" viewBox="0 0 324 268" aria-labelledby="t5">
    <title id="t5">Global perspective</title>
    <rect class="bg" width="324" height="268"/>
    <g class="icon-set">
      <g class="icon-line" stroke-width="4">
        <circle cx="246" cy="56" r="42"/>
        <ellipse cx="246" cy="56" rx="18" ry="42"/>
        <line x1="246" y1="14" x2="246" y2="98"/>
        <line x1="204" y1="56" x2="288" y2="56"/>
        <path d="M211 34h70M211 78h70"/>
      </g>
      <rect class="icon-cut" x="262" y="56" width="48" height="50"/>
      <circle class="icon" cx="288" cy="68" r="11"/>
      <path class="icon" d="M266 104v-8a14 14 0 0 1 14-14h16a14 14 0 0 1 14 14v8z"/>
    </g>
    <g transform="rotate(-16.3 310 135)">
      <rect class="band" x="-120" y="135" width="600" height="44"/>
      <text class="headline" x="281" y="129" text-anchor="end" textLength="159" lengthAdjust="spacingAndGlyphs">GLOBAL</text>
      <text class="band-line" x="261" y="166" text-anchor="end" textLength="159" lengthAdjust="spacingAndGlyphs">PERSPECTIVE</text>
    </g>
    <text class="school-name" x="14" y="174">LINDEN</text>
    <text class="school-name" x="14" y="185">HARBOR</text>
    <text class="school-name" x="14" y="196">ACADEMY</text>
    <text class="footer-name" x="312" y="262" text-anchor="end">Linden Harbor Academy</text>
  </svg>

  <!-- Leadership -->
  <svg class="card card--leadership" viewBox="0 0 324 268" aria-labelledby="t6">
    <title id="t6">Leadership and teamwork</title>
    <rect class="bg" width="324" height="268"/>
    <g class="icon-set">
      <circle class="icon" cx="222" cy="34" r="14"/>
      <path class="icon" d="M198 86v-20a18 18 0 0 1 18-18h12a18 18 0 0 1 18 18v20z"/>
      <circle class="icon" cx="288" cy="34" r="14"/>
      <path class="icon" d="M264 86v-20a18 18 0 0 1 18-18h12a18 18 0 0 1 18 18v20z"/>
      <circle class="icon" cx="255" cy="22" r="15"/>
      <path class="icon" d="M230 80v-22a19 19 0 0 1 19-19h12a19 19 0 0 1 19 19v22z"/>
      <circle class="icon-cut" cx="250" cy="62" r="17"/>
      <circle class="icon" cx="250" cy="62" r="14"/>
      <path class="icon-cut" d="M220 120v-22a22 22 0 0 1 22-22h16a22 22 0 0 1 22 22v22z"/>
      <path class="icon" d="M223 120v-20a20 20 0 0 1 20-20h14a20 20 0 0 1 20 20v20z"/>
    </g>
    <g transform="rotate(-16.3 310 135)">
      <rect class="band" x="-120" y="135" width="600" height="44"/>
      <text class="headline" x="306" y="129" text-anchor="end" textLength="220" lengthAdjust="spacingAndGlyphs">LEADERSHIP</text>
      <text class="band-line" x="287" y="166" text-anchor="end" textLength="210" lengthAdjust="spacingAndGlyphs">AND TEAMWORK</text>
    </g>
    <text class="school-name" x="14" y="174">LINDEN</text>
    <text class="school-name" x="14" y="185">HARBOR</text>
    <text class="school-name" x="14" y="196">ACADEMY</text>
    <text class="footer-name" x="312" y="262" text-anchor="end">Linden Harbor Academy</text>
  </svg>

  <!-- Digital -->
  <svg class="card card--digital" viewBox="0 0 324 268" aria-labelledby="t7">
    <title id="t7">Digital and quantitative literacy</title>
    <rect class="bg" width="324" height="268"/>
    <g class="icon-set">
      <circle class="icon" cx="260" cy="48" r="38"/>
      <path class="icon" d="M236 76h46v30h-46z"/>
      <circle class="icon-line" cx="246" cy="44" r="9" stroke-width="5" style="stroke:var(--bg)" stroke-dasharray="3.5 3.5"/>
      <circle class="icon-cut" cx="246" cy="44" r="5"/>
      <circle class="icon-line" cx="268" cy="36" r="11" stroke-width="6" style="stroke:var(--bg)" stroke-dasharray="4 4"/>
      <circle class="icon-cut" cx="268" cy="36" r="6"/>
      <circle class="icon" cx="268" cy="36" r="3"/>
    </g>
    <g transform="rotate(-16.3 310 135)">
      <rect class="band" x="-120" y="135" width="600" height="44"/>
      <text class="headline" x="279" y="129" text-anchor="end" textLength="156" lengthAdjust="spacingAndGlyphs">DIGITAL</text>
      <text class="band-line" x="303" y="166" text-anchor="end" textLength="241" lengthAdjust="spacingAndGlyphs">AND QUANTITATIVE</text>
      <text class="sub-line" x="242" y="201" text-anchor="end" textLength="95" lengthAdjust="spacingAndGlyphs">LITERACY</text>
    </g>
    <text class="school-name" x="14" y="174">LINDEN</text>
    <text class="school-name" x="14" y="185">HARBOR</text>
    <text class="school-name" x="14" y="196">ACADEMY</text>
    <text class="footer-name" x="312" y="262" text-anchor="end">Linden Harbor Academy</text>
  </svg>

</main>
</body>
</html>
```